Wine Label Design

A wine label for 750ml bottles. Same label for different varieties with the variety / region / vintage to be updated as required.
Brand: Beyond the Ridge
Product Use: Front and Back label suitable for a 750 ml bottle (preferably Burgundy bottles)
Design Brief: Beyond the Ridge is a small winery that produces limited amounts of hand crafted wines that are aimed at the mid to top end of the market and requires a label befitting the work that goes into the creation of the wine. In terms of style i don't have any preconceptions and am open to a broad range of design suggestions at the same level of existing premium brands or innovative brands.
Must Have for Front label
Front Label
Beyond the Ridge
2013
Grampians
Shiraz
750ML (should be in smaller text)
Alc. 14% by Vol. (should be in smaller text)
Must Have for Back Label
Beyond the Ridge
2013
Grampians
Shiraz
www.beyondtheridge.com.au (should be in smaller text)
Product of Australia
Alc.14% by Vol. (should be in smaller text)
Contains preservative 220(should be in smaller text)
Below are some guides for dimensions:
The Front Label Size can be between
100 - 120 mm (Width) x 70 - 85 mm (Height)
The back label size can be between
90 mm (Width) x 70 - 85 mm (Height)
Target Market(s)
Medium to top end of the wine market who require the label to be a reflection of the wine.
Industry/Entity Type
Product
Colors
Designer to choose colors to be used in the design.
Look and feel

```html
<!DOCTYPE html>
<html lang="en">
<head>
<meta charset="utf-8">
<title>Beyond the Ridge – Grampians Shiraz 2013</title>
<link href="https://fonts.googleapis.com/css2?family=Just+Another+Hand&family=Amatic+SC:wght@400&display=block" rel="stylesheet">
<style>
  :root {
    --paper: #ffffff;
    --ink: #1a1a1a;
    --sketch-mid: #d6d6d6;
    --sketch-light: #f1f1f1;
  }
  * { margin: 0; padding: 0; box-sizing: border-box; }
  html, body {
    width: 1200px;
    height: 931px;
    overflow: hidden;
    background: var(--paper);
  }
  .label {
    position: relative;
    width: 1200px;
    height: 931px;
    background: var(--paper);
    color: var(--ink);
    font-family: "Just Another Hand", "Amatic SC", sans-serif;
    font-weight: 400;
  }
  .label__line {
    position: absolute;
    left: 0;
    width: 1260px;
    text-align: center;
    line-height: 1;
    white-space: nowrap;
    font-weight: 400;
    font-style: normal;
  }
  .brand-name {
    top: 58px;
    font-size: 78px;
    letter-spacing: 1px;
  }
  .vineyard-scene {
    position: absolute;
    left: 490px;
    top: 150px;
    width: 284px;
    height: 164px;
    border-radius: 50% 50% 30% 30% / 55% 55% 20% 20%;
    background: linear-gradient(180deg, var(--sketch-light) 0%, var(--sketch-mid) 60%, var(--sketch-light) 100%);
  }
  .region   { top: 344px; font-size: 36px; }
  .variety  { top: 386px; font-size: 36px; }
  .vintage  { top: 474px; font-size: 36px; }
  .website  { top: 584px; font-size: 50px; }
  .origin   { top: 666px; font-size: 88px; }
  .volume        { top: 786px; font-size: 34px; }
  .alcohol       { top: 826px; font-size: 34px; }
  .preservative  { top: 866px; font-size: 34px; }
</style>
</head>
<body>
  <main class="label">
    <h1 class="label__line brand-name">BEYOND THE RIDGE</h1>
    <div class="vineyard-scene" role="img" aria-label="Pen sketch of rolling vineyard hills with a farmhouse, tall cypress trees and a fence"></div>
    <p class="label__line region">GRAMPIANS</p>
    <p class="label__line variety">SHIRAZ</p>
    <p class="label__line vintage">2013</p>
    <p class="label__line website">www.beyondtheridge.com.au</p>
    <p class="label__line origin">Product of Australia</p>
    <p class="label__line volume">750ML</p>
    <p class="label__line alcohol">Alc.14% by Vol</p>
    <p class="label__line preservative">Contains preservative 220</p>
  </main>
</body>
</html>
```